Tree Pruning Website

We need a website for a tree Arborist, pruning company called Hollow Ridge Branchworks. We look after all types of trees, knock down trees and prune trees. Our target market is from domestic clients to government clients and everything in between.

We would like to see the use of our main colours which are orange and green

We are not looking forward in seeing a template that we have seen before but a unique template. We have designed 5 templates ourselves and we wish for the design community to take our designs to the next level.

We have also designed a template for things that **we are not** looking for (Version 4)

To make it fair for everyone, we are also not giving out any participation payments as we have had. One winner will take all of the payment!!!

I Have attached a image of the designs and a image of a tree.

We are just looking at the PSD file been developed. We have our own team who can slice the image up into a HTML format.

Target Market(s)

Everyone who needs to cut down a tree

Industry/Entity Type

Government

Requirements
Must have
• Logo on front page
A List of our services
jQuery slider on page
Phone Number on every page

```html
<!DOCTYPE html>
<html lang="en">
<head>
<meta charset="utf-8">
<title>Hollow Ridge Branchworks</title>
<link rel="stylesheet" href="https://fonts.googleapis.com/css2?family=Arvo:wght@700&family=Oswald:wght@300;400;500&family=Open+Sans:wght@400;600&display=swap">
<style>
:root{
  --wood-dark:#2a1a10;
  --wood-mid:#4a3020;
  --wood-light:#5d3d28;
  --orange:#f5a800;
  --orange-deep:#e89400;
  --green:#2f9a12;
  --green-dark:#1d6f08;
  --tan:#e9d2ac;
  --tan-light:#f0dcba;
  --text-dark:#3a2a1a;
  --text-body:#6b5a45;
  --cream:#f4e9d8;
  --white:#ffffff;
}
*{margin:0;padding:0;box-sizing:border-box}
html,body{width:891px;height:1200px;overflow:hidden}
body{font-family:"Open Sans",Arial,sans-serif;background:#fff}
.page{position:relative;width:891px;height:1200px;overflow:hidden}
.abs{position:absolute}

.topbar{left:0;top:0;width:891px;height:48px;
  background:repeating-linear-gradient(90deg,var(--wood-dark) 0 3px,#33210f 3px 7px,#2c1b0e 7px 12px);}
.brand{left:103px;top:0;width:94px;height:116px;background:var(--white);z-index:3;
  display:flex;flex-direction:column;align-items:center;justify-content:center;gap:8px;box-shadow:0 2px 6px rgba(0,0,0,.35)}
.brand-dot{width:30px;height:30px;border-radius:50%;background:var(--green)}
.brand-name{font-family:"Oswald",sans-serif;font-weight:300;font-size:13px;line-height:15px;color:var(--green-dark);text-align:center}
.nav{left:229px;top:0;height:48px;z-index:2}
.nav a{font-family:"Oswald",sans-serif;font-weight:300;font-size:14px;color:var(--cream);text-decoration:none;line-height:50px;position:absolute;white-space:nowrap}
.nav a.active{color:var(--orange)}
.call{left:657px;top:0;width:131px;height:48px;background:var(--orange);text-align:center;color:var(--white);z-index:2}
.call small{display:flex;justify-content:center;align-items:center;gap:4px;font-family:"Oswald",sans-serif;font-size:10px;color:var(--text-dark);padding-top:5px}
.call strong{display:block;font-family:"Oswald",sans-serif;font-weight:500;font-size:19px;line-height:22px}

.hero{left:0;top:48px;width:891px;height:420px;
  background:radial-gradient(ellipse at 75% 55%,#6b5a3e 0 14%,transparent 30%),
  linear-gradient(180deg,#3d5a22 0%,#2a4317 40%,#1f3312 75%,#35501f 100%)}
.hero-title{left:103px;top:186px;display:flex;align-items:center;gap:6px}
.hero-title .big{font-family:"Arvo",serif;font-weight:700;font-size:50px;color:var(--orange);letter-spacing:-1px;line-height:54px}
.hero-title .small{font-family:"Arvo",serif;font-weight:700;font-size:21px;color:var(--white);line-height:25px}
.hero-copy{left:103px;top:252px;width:416px;font-size:9.6px;line-height:13px;color:var(--white)}
.quote-btn{left:103px;top:323px;width:227px;height:51px;background:linear-gradient(180deg,#4cc01c,var(--green-dark));
  font-family:"Oswald",sans-serif;font-weight:400;font-size:28px;color:var(--white);text-align:center;line-height:51px}
.dots{left:420px;top:459px;display:flex;gap:3px;z-index:2}
.dots span{width:16px;height:16px;border-radius:50%;background:var(--white);border:2px solid var(--white)}
.dots span.on{background:#333;box-shadow:inset 0 0 0 2px var(--white)}

.sectors{left:0;top:468px;width:891px;height:193px;background:linear-gradient(180deg,var(--orange),var(--orange-deep))}
.sector{position:absolute;top:41px;width:163px;text-align:center}
.sector .thumb{width:163px;height:101px;border:3px solid var(--white)}
.sector p{font-family:"Oswald",sans-serif;font-weight:300;font-size:14px;color:var(--text-dark);margin-top:14px}

.content{left:0;top:661px;width:891px;height:317px;background:linear-gradient(180deg,var(--tan-light),var(--tan))}
.welcome{left:104px;top:727px;display:flex;align-items:center;gap:8px}
.welcome .mark{width:20px;height:20px;border-radius:50%;border:3px solid var(--orange)}
.welcome h1{font-family:"Oswald",sans-serif;font-weight:300;font-size:21px;color:var(--green-dark)}
.welcome h1 span{color:var(--text-dark)}
.intro{left:103px;top:762px;width:505px;font-size:12px;line-height:16px;color:var(--text-dark)}
.body{left:103px;top:804px;width:500px;font-size:8.6px;line-height:13px;color:var(--text-body);text-align:justify}
.services{left:637px;top:719px;width:148px;height:195px;background:var(--white);box-shadow:3px 3px 0 #ddd,5px 5px 6px rgba(0,0,0,.2);padding:10px 0 0 20px}
.services h2{font-family:"Oswald",sans-serif;font-weight:300;font-size:20px;color:var(--green-dark);margin-bottom:8px}
.services h2 span{color:var(--text-dark)}
.services li{list-style:none;font-size:9px;line-height:16.4px;color:var(--text-dark);display:flex;align-items:center;gap:9px}
.services li::before{content:"";width:7px;height:7px;background:var(--green);display:block;clip-path:polygon(0 0,100% 50%,0 100%)}

.footer{left:0;top:978px;width:891px;height:183px;
  background:repeating-linear-gradient(90deg,var(--wood-mid) 0 4px,var(--wood-light) 4px 9px,#452c1c 9px 15px)}
.foot-h{font-family:"Oswald",sans-serif;font-weight:300;font-size:17px;color:var(--orange)}
.sitemap{left:103px;top:1002px}
.sitemap ul{margin-top:8px}
.sitemap li{list-style:none;font-size:8.5px;line-height:16.4px;color:var(--cream)}
.gallery{left:220px;top:1002px}
.gallery .grid{display:grid;grid-template-columns:repeat(3,53px);gap:5px;margin-top:10px}
.gallery .grid div{height:42px;border:2px solid var(--white)}
.contact{left:439px;top:1002px}
.contact .map{width:189px;height:93px;margin-top:10px;background:linear-gradient(135deg,#e7e7e2,#cfd7d9)}
.reach{left:662px;top:1034px;color:var(--cream)}
.reach .row{display:flex;align-items:center;gap:8px;position:absolute;left:0;white-space:nowrap}
.reach .ic{width:19px;height:19px;border-radius:50%;background:var(--green);display:flex;align-items:center;justify-content:center}
.reach .addr{font-size:12px;line-height:16px}
.reach .tel{font-family:"Oswald",sans-serif;font-weight:500;font-size:17px;line-height:22px}
.tree-art{left:683px;top:1140px;width:106px;height:60px;border-radius:50% 50% 0 0;background:radial-gradient(ellipse at 50% 35%,#4a9a2a,#2e6d16)}
.copy{left:0;top:1161px;width:891px;height:39px;background:var(--wood-dark);font-size:8.5px;color:#a99580;text-align:center;line-height:39px}
</style>
</head>
<body>
<div class="page">
  <div class="abs topbar"></div>
  <div class="abs brand"><span class="brand-dot"></span><span class="brand-name">Hollow Ridge<br>Branchworks</span></div>
  <nav class="abs nav">
    <a class="active" style="left:0">Home</a>
    <a style="left:54px">About Us</a>
    <a style="left:122px">Our Services</a>
    <a style="left:204px">Our Work</a>
    <a style="left:275px">Get a Quote</a>
    <a style="left:355px">Contact Us</a>
  </nav>
  <div class="abs call">
    <small><svg width="10" height="10" viewBox="0 0 24 24"><path fill="#3a2a1a" d="M6.6 10.8a15 15 0 006.6 6.6l2.2-2.2c.3-.3.7-.4 1-.2 1.1.4 2.3.6 3.6.6.6 0 1 .4 1 1V20c0 .6-.4 1-1 1A17 17 0 013 4c0-.6.4-1 1-1h3.5c.6 0 1 .4 1 1 0 1.3.2 2.5.6 3.6.1.3 0 .7-.2 1z"/></svg>Contact Now</small>
    <strong>08 7420 5531</strong>
  </div>

  <div class="abs hero" role="img" aria-label="Forest scene with a person hugging a large tree trunk"></div>
  <div class="abs hero-title"><span class="big">HOLLOW</span><span class="small">Ridge<br>Branchworks</span></div>
  <p class="abs hero-copy">Lorem Ipsum is simply dummy text of the printing and typesetting industry. Lorem Ipsum has been the industry's standard dummy text ever since the 1500s, when an unknown printer took a galley of type and scrambled it to make a type specimen book. It has survived not only five centuries, but also the leap into electronic typesetting, remaining essentially unchanged.</p>
  <div class="abs quote-btn">GET A QUOTE</div>
  <div class="abs dots"><span></span><span class="on"></span><span></span></div>

  <section class="abs sectors">
    <div class="sector" style="left:103px"><div class="thumb" role="img" aria-label="Arborist pruning a tree in a garden" style="background:linear-gradient(160deg,#9bbf6a,#4f7a2e)"></div><p>Domestic</p></div>
    <div class="sector" style="left:277px"><div class="thumb" role="img" aria-label="Office building with street trees" style="background:linear-gradient(160deg,#9ac4e6,#7b8a8f 60%,#4b7a3a)"></div><p>Commercial</p></div>
    <div class="sector" style="left:451px"><div class="thumb" role="img" aria-label="Worker beside a fallen tree trunk" style="background:linear-gradient(160deg,#6f7d5a,#3e4a2c)"></div><p>Goverment</p></div>
    <div class="sector" style="left:624px"><div class="thumb" role="img" aria-label="Hands holding a small tree sapling" style="background:linear-gradient(160deg,#5e5546,#2e2a22)"></div><p>Non Profit</p></div>
  </section>

  <section class="abs content"></section>
  <div class="abs welcome"><span class="mark"></span><h1>Welcome to <span>Hollow Ridge Branchworks</span></h1></div>
  <p class="abs intro">Hollow Ridge is the leading tree purning services located Perth. Our motto is when you call, we gurrantee to turn up and provide care to our customers.</p>
  <p class="abs body">Our crew handles every tree job from a single backyard gum to a full council streetscape. We assess health, plan each cut and leave the site tidy when we go. Every arborist on the team holds current training and insurance, and we follow the national standard for pruning amenity trees. Whether a limb hangs over a roof, roots lift a path or storm damage needs fast work, we arrive on time with the right gear. Ask us for a free site visit and a written quote with no hidden costs, then let us care for the trees you value most. Call today.</p>
  <aside class="abs services">
    <h2>Our <span>Services</span></h2>
    <ul>
      <li>Diagnosis</li><li>Treatment</li><li>Purning</li><li>Tree Removal</li><li>Stump Removal</li><li>Cabling &amp; Bracing</li><li>Arborist Consults</li><li>Tree Protection</li>
    </ul>
  </aside>

  <footer class="abs footer"></footer>
  <div class="abs sitemap"><h3 class="foot-h">Site Map</h3>
    <ul><li>Home</li><li>About Us</li><li>Our Services</li><li>Our Work</li><li>Get a Quote</li><li>Contact Us</li></ul></div>
  <div class="abs gallery"><h3 class="foot-h">Work Gallery</h3>
    <div class="grid" role="img" aria-label="Six photos of tree work">
      <div style="background:#6d7c55"></div><div style="background:#4e6a36"></div><div style="background:#5b5e4c"></div>
      <div style="background:#7f9b5a"></div><div style="background:#5f8a38"></div><div style="background:#b9ab8e"></div>
    </div></div>
  <div class="abs contact"><h3 class="foot-h">Contact Us</h3>
    <div class="map" role="img" aria-label="Street map of the office location"></div></div>
  <div class="abs reach">
    <div class="row" style="top:0"><span class="ic"><svg width="10" height="12" viewBox="0 0 20 24"><path fill="#fff" d="M10 0a8 8 0 00-8 8c0 6 8 16 8 16s8-10 8-16a8 8 0 00-8-8zm0 11a3 3 0 110-6 3 3 0 010 6z"/></svg></span><span class="addr">41 Marlow Lane,<br>Brookvale, WA 6190</span></div>
    <div class="row" style="top:46px"><span class="ic"><svg width="11" height="11" viewBox="0 0 24 24"><path fill="#fff" d="M6.6 10.8a15 15 0 006.6 6.6l2.2-2.2c.3-.3.7-.4 1-.2 1.1.4 2.3.6 3.6.6.6 0 1 .4 1 1V20c0 .6-.4 1-1 1A17 17 0 013 4c0-.6.4-1 1-1h3.5c.6 0 1 .4 1 1 0 1.3.2 2.5.6 3.6.1.3 0 .7-.2 1z"/></svg></span><span class="tel">08 7420 5532</span></div>
    <div class="row" style="top:74px"><span class="ic"><svg width="11" height="11" viewBox="0 0 24 24"><rect x="3" y="6" width="18" height="14" rx="2" fill="#fff"/><rect x="7" y="2" width="10" height="6" fill="#fff"/></svg></span><span class="tel">08 7420 5533</span></div>
  </div>
  <div class="abs tree-art" role="img" aria-label="Illustrated green tree"></div>
  <div class="abs copy">Copyright © Hollow Ridge Branchworks</div>
</div>
</body>
</html>
```